Valtrix PowerPoint Templates

We need a cover page and body page templates for a complete Powerpoint presentation. We administer workers' compensation claims in California mostly to public entities. We offer cloud based software to develop and communicate all the data for each claim. Although we are a technology company, we also see ourselves as the human interface working closely with the client and injured workers.
It all starts with our Logo!
We want to loosely relate our Powerpoint design with our Logo. Maybe just in the color! WE DONT WANT TO RECREATE OUR LOGO AS A PROPOSAL . I've posted the logo and a rough proposal page for reference. We designed it using ArtHive and feel the designer met our criteria very well. As I recall the spec for the logo was to use our name and incorporate "modern, professional and personal" into the design. We will use this template to attract new business. We will be approaching a variety of industries and want the template to be designed specifically for our business identity rather than for clients we are pursuing.
I will also post a simple example of a competitor's PowerPoint presentation for reference.
Please feel free to ask any questions you may have.
Thank You!
Gordon

Industry/Entity Type

Software

```html
<!DOCTYPE html>
<html lang="en">
<head>
<meta charset="utf-8">
<title>Valtrix – What We Do</title>
<link rel="stylesheet" href="https://fonts.googleapis.com/css2?family=Open+Sans:wght@400;700&family=Roboto+Condensed:wght@600&display=swap">
<style>
  :root {
    --ink: #4a4a4a;
    --logo-ink: #5f6064;
    --blue: #3d6db5;
    --blue-bright: #1fa9ea;
    --blue-deep: #1675c4;
    --black: #0b0b0b;
    --white: #ffffff;
    --shadow: #c9c9c9;
  }
  * { margin: 0; padding: 0; box-sizing: border-box; }
  html, body { width: 1200px; height: 900px; overflow: hidden; background: var(--white); }
  .slide { position: relative; width: 1200px; height: 900px; overflow: hidden; background: var(--white); }

  .header-pattern {
    position: absolute; left: 0; top: 0; width: 700px; height: 90px;
    background: linear-gradient(100deg, rgba(30,110,190,0.75) 0%, rgba(90,170,230,0.45) 35%, rgba(150,200,235,0.25) 65%, rgba(255,255,255,0) 100%);
  }

  .brand { position: absolute; right: 26px; top: 28px; text-align: left; }
  .brand-name {
    font-family: "Open Sans", sans-serif; font-weight: 700; font-size: 52px;
    line-height: 1; color: var(--logo-ink); letter-spacing: -1px;
  }
  .brand-tagline {
    font-family: "Open Sans", sans-serif; font-weight: 400; font-size: 14px;
    color: var(--logo-ink); margin-top: 6px;
  }

  .rule-accent { position: absolute; left: 0; top: 109px; width: 146px; height: 8px; background: var(--blue); }
  .rule-main { position: absolute; left: 157px; top: 109px; width: 1043px; height: 8px; background: var(--black); }

  .section-badge { position: absolute; left: 30px; top: 148px; width: 270px; height: 300px; }
  .section-badge text {
    font-family: "Open Sans", sans-serif; font-weight: 700; font-size: 25px; fill: var(--white);
  }

  .body-copy {
    position: absolute; left: 181px; top: 470px; width: 905px;
    font-family: "Roboto Condensed", sans-serif; font-weight: 600; font-size: 26.5px;
    line-height: 33px; color: var(--ink);
  }
  .body-copy p + p { margin-top: 33px; }

  .footer-rule { position: absolute; left: 0; top: 828px; width: 1200px; height: 9px; background: var(--black); }
  .footer-band { position: absolute; left: 0; top: 837px; width: 1200px; height: 63px; background: var(--blue); }
</style>
</head>
<body>
<main class="slide">
  <div class="header-pattern" role="img" aria-label="Decorative mosaic of scattered blue squares"></div>

  <div class="brand">
    <div class="brand-name">Valtrix</div>
    <div class="brand-tagline">Claims Management Solutions</div>
  </div>

  <div class="rule-accent"></div>
  <div class="rule-main"></div>

  <svg class="section-badge" viewBox="0 0 270 300" aria-hidden="true">
    <defs>
      <radialGradient id="badge-fill" cx="45%" cy="40%" r="65%">
        <stop offset="0%" stop-color="var(--blue-bright)"/>
        <stop offset="100%" stop-color="var(--blue-deep)"/>
      </radialGradient>
      <radialGradient id="badge-shadow" cx="50%" cy="50%" r="50%">
        <stop offset="0%" stop-color="#bdbdbd"/>
        <stop offset="100%" stop-color="#e8e8e8" stop-opacity="0"/>
      </radialGradient>
    </defs>
    <ellipse cx="134" cy="258" rx="104" ry="24" fill="url(#badge-shadow)"/>
    <ellipse cx="131" cy="114" rx="126" ry="110" fill="url(#badge-fill)"/>
    <text x="131" y="123" text-anchor="middle">WHAT WE DO</text>
  </svg>

  <section class="body-copy">
    <p>We have developed what we feel are the optimum philosophies, procedures and work flow to support those philosophies.</p>
    <p>We feel that all of these elements combined allow us to assist our clients in obtaining optimal results on their Workers’ Compensation programs</p>
  </section>

  <div class="footer-rule"></div>
  <div class="footer-band"></div>
</main>
</body>
</html>
```